Property Management Company looking for a high-end business card, letterhead and envelope design.

We provide high-end / boutique property management for real estate investors or individuals looking for someone to manage their portfolio. we are looking for a cohesive high-end design for our business cards, letterhead and envelopes.

Target Market(s)

Real Estate Investors

Industry/Entity Type

Real Estate

Requirements
Must have
• business card, letterhead and envelope design - logo attached

```html
<!DOCTYPE html>
<html lang="en">
<head>
<meta charset="utf-8">
<title>Harborline Property Management – Stationery</title>
<link href="https://fonts.googleapis.com/css2?family=Montserrat:wght@400;500;700&display=swap" rel="stylesheet">
<style>
  :root {
    --backdrop: #353a45;
    --paper: #ffffff;
    --brand-blue: #0a4f84;
    --accent-grey: #a3a3a3;
    --text-dark: #3c3c3c;
  }
  * { margin: 0; padding: 0; box-sizing: border-box; }
  html, body { width: 1200px; height: 828px; overflow: hidden; }
  body {
    background: var(--backdrop);
    position: relative;
    font-family: "Montserrat", sans-serif;
  }
  .sheet {
    position: absolute;
    background: var(--paper);
    overflow: hidden;
  }
  .sheet > .shapes {
    position: absolute; inset: 0; width: 100%; height: 100%;
  }
  .brand { position: absolute; line-height: 1; }
  .brand-name {
    display: block;
    font-weight: 700;
    color: var(--brand-blue);
    letter-spacing: 0.14em;
  }
  .brand-tagline {
    display: block;
    font-weight: 500;
    color: var(--brand-blue);
    letter-spacing: 0.2em;
  }
  .brand.on-blue .brand-name,
  .brand.on-blue .brand-tagline { color: var(--paper); }

  .contact-list { position: absolute; list-style: none; }
  .contact-list li {
    display: flex; align-items: center;
    color: var(--text-dark);
    white-space: nowrap;
  }
  .contact-list svg { flex: none; }

  /* Letterhead */
  .letterhead { left: 185px; top: 153px; width: 400px; height: 518px; }
  .letterhead .brand { left: 38px; top: 17px; }
  .letterhead .brand-name { font-size: 13.5px; }
  .letterhead .brand-tagline { font-size: 6.4px; margin-top: 3px; }
  .letterhead .contact-list { top: 481px; font-size: 6.6px; }
  .letterhead .contact-list li { height: 13px; gap: 9px; }
  .letterhead .contact-list svg { width: 9px; height: 9px; }
  .letterhead .col-left { left: 38px; }
  .letterhead .col-right { left: 192px; }

  /* Business cards */
  .card { width: 147px; height: 84px; }
  .card-front-a { left: 639px; top: 214px; }
  .card-back-a  { left: 815px; top: 214px; }
  .card-back-b  { left: 639px; top: 326px; }
  .card-front-b { left: 815px; top: 326px; }
  .card-front .brand { left: 0; right: 0; top: 34px; text-align: center; padding-left: 2px; }
  .card-front .brand-name { font-size: 10px; }
  .card-front .brand-tagline { font-size: 4.2px; margin-top: 1.5px; }
  .card-back .brand { left: 39px; top: 10px; }
  .card-back .brand-name { font-size: 9.2px; }
  .card-back .brand-tagline { font-size: 4.2px; margin-top: 1.5px; }
  .card-back .contact-list { left: 39px; top: 41px; font-size: 3.9px; }
  .card-back .contact-list li { height: 8.6px; gap: 6px; }
  .card-back .contact-list svg { width: 5px; height: 5px; }

  /* Envelope */
  .envelope { left: 619px; top: 484px; width: 371px; height: 187px; }
  .envelope .brand { left: 33px; top: 15px; }
  .envelope .brand-name { font-size: 13.5px; }
  .envelope .brand-tagline { font-size: 6.4px; margin-top: 3px; }
  .envelope .contact-list { top: 154px; font-size: 6.6px; }
  .envelope .contact-list li { height: 13px; gap: 9px; }
  .envelope .contact-list svg { width: 9px; height: 9px; }
  .envelope .col-left { left: 33px; }
  .envelope .col-right { left: 187px; }
</style>
</head>
<body>

<svg width="0" height="0" style="position:absolute" aria-hidden="true">
  <defs>
    <symbol id="icon-phone" viewBox="0 0 20 20">
      <circle cx="10" cy="10" r="10" fill="#0a4f84"/>
      <path d="M6.5 5.5 L8.5 5 L9.5 7.5 L8.3 8.5 Q9.3 10.8 11.5 11.7 L12.5 10.5 L15 11.5 L14.5 13.5 Q9 14.5 6.5 5.5 Z" fill="#fff"/>
    </symbol>
    <symbol id="icon-pin" viewBox="0 0 20 20">
      <circle cx="10" cy="10" r="10" fill="#0a4f84"/>
      <path d="M10 4.5 A3.8 3.8 0 0 1 13.8 8.3 Q13.8 10.8 10 15.5 Q6.2 10.8 6.2 8.3 A3.8 3.8 0 0 1 10 4.5 Z" fill="#fff"/>
      <circle cx="10" cy="8.3" r="1.5" fill="#0a4f84"/>
    </symbol>
    <symbol id="icon-web" viewBox="0 0 20 20">
      <circle cx="10" cy="10" r="10" fill="#0a4f84"/>
      <g fill="none" stroke="#fff" stroke-width="1">
        <circle cx="10" cy="10" r="5"/>
        <ellipse cx="10" cy="10" rx="2.2" ry="5"/>
        <line x1="5" y1="10" x2="15" y2="10"/>
      </g>
    </symbol>
    <symbol id="icon-mail" viewBox="0 0 20 20">
      <circle cx="10" cy="10" r="10" fill="#0a4f84"/>
      <rect x="5.5" y="6.8" width="9" height="6.4" fill="#fff"/>
      <path d="M5.5 6.8 L10 10.5 L14.5 6.8" fill="none" stroke="#0a4f84" stroke-width="0.9"/>
    </symbol>
  </defs>
</svg>

<!-- Letterhead -->
<section class="sheet letterhead">
  <svg class="shapes" viewBox="0 0 400 518" preserveAspectRatio="none" aria-hidden="true">
    <polygon points="0,0 42,0 0,56" fill="var(--brand-blue)"/>
    <polygon points="327,518 400,518 400,447" fill="var(--accent-grey)"/>
  </svg>
  <div class="brand">
    <span class="brand-name">HARBORLINE</span>
    <span class="brand-tagline">PROPERTY MANAGEMENT</span>
  </div>
  <ul class="contact-list col-left">
    <li><svg><use href="#icon-phone"/></svg>+15550102046</li>
    <li><svg><use href="#icon-pin"/></svg>48 Linden Row NE Ridgeford</li>
  </ul>
  <ul class="contact-list col-right">
    <li><svg><use href="#icon-web"/></svg>www.harborlinepm.com</li>
    <li><svg><use href="#icon-mail"/></svg>mail@harborlinepm.com</li>
  </ul>
</section>

<!-- Business card front -->
<section class="sheet card card-front card-front-a">
  <svg class="shapes" viewBox="0 0 147 84" preserveAspectRatio="none" aria-hidden="true">
    <polygon points="49,0 147,0 147,62 131,84 0,84 0,64" fill="var(--brand-blue)"/>
  </svg>
  <div class="brand on-blue">
    <span class="brand-name">HARBORLINE</span>
    <span class="brand-tagline">PROPERTY MANAGEMENT</span>
  </div>
</section>

<!-- Business card back -->
<section class="sheet card card-back card-back-a">
  <svg class="shapes" viewBox="0 0 147 84" preserveAspectRatio="none" aria-hidden="true">
    <polygon points="0,0 33,0 0,44" fill="var(--brand-blue)"/>
    <polygon points="131,84 147,84 147,62" fill="var(--accent-grey)"/>
  </svg>
  <div class="brand">
    <span class="brand-name">HARBORLINE</span>
    <span class="brand-tagline">PROPERTY MANAGEMENT</span>
  </div>
  <ul class="contact-list">
    <li><svg><use href="#icon-phone"/></svg>+15550102046</li>
    <li><svg><use href="#icon-pin"/></svg>48 Linden Row NE Ridgeford</li>
    <li><svg><use href="#icon-web"/></svg>www.harborlinepm.com</li>
    <li><svg><use href="#icon-mail"/></svg>mail@harborlinepm.com</li>
  </ul>
</section>

<!-- Business card back -->
<section class="sheet card card-back card-back-b">
  <svg class="shapes" viewBox="0 0 147 84" preserveAspectRatio="none" aria-hidden="true">
    <polygon points="0,0 33,0 0,44" fill="var(--brand-blue)"/>
    <polygon points="131,84 147,84 147,62" fill="var(--accent-grey)"/>
  </svg>
  <div class="brand">
    <span class="brand-name">HARBORLINE</span>
    <span class="brand-tagline">PROPERTY MANAGEMENT</span>
  </div>
  <ul class="contact-list">
    <li><svg><use href="#icon-phone"/></svg>+15550102046</li>
    <li><svg><use href="#icon-pin"/></svg>48 Linden Row NE Ridgeford</li>
    <li><svg><use href="#icon-web"/></svg>www.harborlinepm.com</li>
    <li><svg><use href="#icon-mail"/></svg>mail@harborlinepm.com</li>
  </ul>
</section>

<!-- Business card front -->
<section class="sheet card card-front card-front-b">
  <svg class="shapes" viewBox="0 0 147 84" preserveAspectRatio="none" aria-hidden="true">
    <polygon points="49,0 147,0 147,62 131,84 0,84 0,64" fill="var(--brand-blue)"/>
  </svg>
  <div class="brand on-blue">
    <span class="brand-name">HARBORLINE</span>
    <span class="brand-tagline">PROPERTY MANAGEMENT</span>
  </div>
</section>

<!-- Envelope -->
<section class="sheet envelope">
  <svg class="shapes" viewBox="0 0 371 187" preserveAspectRatio="none" aria-hidden="true">
    <polygon points="0,0 30,0 0,40" fill="var(--brand-blue)"/>
    <polygon points="330,187 371,187 371,132" fill="var(--accent-grey)"/>
  </svg>
  <div class="brand">
    <span class="brand-name">HARBORLINE</span>
    <span class="brand-tagline">PROPERTY MANAGEMENT</span>
  </div>
  <ul class="contact-list col-left">
    <li><svg><use href="#icon-phone"/></svg>+15550102046</li>
    <li><svg><use href="#icon-pin"/></svg>48 Linden Row NE Ridgeford</li>
  </ul>
  <ul class="contact-list col-right">
    <li><svg><use href="#icon-web"/></svg>www.harborlinepm.com</li>
    <li><svg><use href="#icon-mail"/></svg>mail@harborlinepm.com</li>
  </ul>
</section>

</body>
</html>
```